Looking to build a senior life alert web page

We definitely want to incorporate pictures of the product in which we're selling and want colors that resonate with the senior community. We're looking for something also clean and very easy to navigate. We're looking to pick a design immediately!
Based on something similar to that of our competition which can be located at the following
https://www.corvenhelpline.com/
https://www.trellowatch.com/

attached is the product we're selling

The name of our company is the elder harbor circle

Target Market(s)

Elderly people looking for a life alert device

Industry/Entity Type

Medical Equipment

Number of Pages Required

3 page

Font styles to use
Serif

Colors

Designer to choose colors to be used in the design.

Requirements
Must have
• Pictures of the product a nice UI experience that can be easily made mobile friendly
Nice to have
• Including area for video content maybe / friendly color LOGOS are attached for our company

```html
<!DOCTYPE html>
<html lang="en">
<head>
<meta charset="utf-8">
<title>Elder Harbor Circle — Personal Alert Device</title>
<link href="https://fonts.googleapis.com/css2?family=Montserrat:wght@300;400;600;700;800&family=Open+Sans:wght@400;600&display=swap" rel="stylesheet">
<style>
:root{
  --blue:#4a8fe7;
  --blue-deep:#2f74d0;
  --orange:#f7a531;
  --ink:#2b2f36;
  --muted:#7a808a;
  --line:#e3e6eb;
  --dark:#1c231c;
  --paper:#ffffff;
  --mist:#f3f4f6;
  --device:#f4f6f8;
  --device-shade:#c9d0d8;
  --alert-red:#d83a3a;
  --skin:#f1cdb0;
}
*{box-sizing:border-box;margin:0;padding:0}
html,body{width:1200px;height:4663px;overflow:hidden}
body{font-family:"Open Sans",Arial,sans-serif;color:var(--ink);background:var(--paper);position:relative}
.abs{position:absolute}
section,header,footer{position:absolute;left:0;width:1200px;overflow:hidden}
.h-thin{font-family:"Montserrat",Arial,sans-serif;font-weight:300;font-size:22px;letter-spacing:1px;text-transform:uppercase;line-height:1.1}
.h-bold{font-family:"Montserrat",Arial,sans-serif;font-weight:700;font-size:22px;letter-spacing:1px;text-transform:uppercase;line-height:1.1}
.tag{display:inline-block;border:1px solid var(--ink);font-family:"Montserrat",Arial,sans-serif;font-size:11px;font-weight:600;letter-spacing:1px;padding:7px 14px;text-transform:uppercase}
.body-text{font-size:12.5px;line-height:1.75;color:var(--muted)}
.btn{display:inline-block;font-family:"Montserrat",Arial,sans-serif;font-weight:600;font-size:11px;letter-spacing:1px;text-transform:uppercase;border-radius:22px;padding:11px 24px;white-space:nowrap}
.btn-orange{background:var(--orange);color:#fff}
.btn-ghost{border:1.5px solid #fff;color:#fff}
.btn-line{border:1.5px solid var(--ink);color:var(--ink)}

/* product photo areas: soft gradients in the device's tones */
.device-photo{background:
  radial-gradient(ellipse 22% 26% at 50% 38%,rgba(216,58,58,.55),rgba(216,58,58,0) 100%),
  radial-gradient(ellipse 60% 55% at 50% 45%,var(--device) 0%,#e6eaee 60%,rgba(201,208,216,0) 100%)}

/* hero */
.hero{top:0;height:640px;background:var(--paper)}
.hero-bg{position:absolute;left:0;top:0}
.topbar{position:absolute;top:0;left:187px;width:826px;height:34px;display:flex;justify-content:space-between;align-items:center;font-size:10px;color:#fff;letter-spacing:.5px;font-weight:600}
.nav{position:absolute;top:36px;left:187px;width:826px;height:64px;background:#fff;display:flex;align-items:center;padding:0 18px;box-shadow:0 4px 16px rgba(0,0,0,.12)}
.brand{display:flex;align-items:center;gap:8px;font-family:"Montserrat",Arial,sans-serif;font-weight:700;font-size:12px;color:var(--blue-deep);letter-spacing:.5px;text-transform:uppercase;white-space:nowrap}
.brand-dot{width:22px;height:22px;border-radius:50%;background:var(--blue);flex:none}
.menu{display:flex;gap:20px;margin-left:auto;margin-right:22px;font-family:"Montserrat",Arial,sans-serif;font-size:10px;font-weight:600;letter-spacing:.6px}
.menu span{color:var(--muted)}
.menu .on{color:var(--ink);border-bottom:2px solid var(--ink);padding-bottom:3px}
.hero-product{left:180px;top:120px;width:340px;height:320px}
.hero-copy{left:540px;top:215px;width:470px;color:#fff}
.kicker{font-family:"Montserrat",Arial,sans-serif;font-size:11px;letter-spacing:3px;font-weight:600;opacity:.9}
.hero-title{font-family:"Montserrat",Arial,sans-serif;font-weight:800;font-size:31px;line-height:1.15;margin-top:8px;letter-spacing:.5px}
.hero-copy p{font-size:12.5px;line-height:1.6;margin-top:12px;font-weight:600}
.hero-btns{margin-top:22px;display:flex;gap:12px}

/* xtra features */
.xtra{top:620px;height:100px;background:#fff}
.xtra-inner{position:absolute;left:187px;top:28px;width:826px;display:flex;align-items:center}
.xtra-title{font-family:"Montserrat",Arial,sans-serif;font-size:15px;line-height:1.05;letter-spacing:1px;width:170px}
.xtra-title b{display:block;font-weight:700;font-size:14px}
.xtra-item{display:flex;align-items:center;gap:14px;width:164px;font-family:"Montserrat",Arial,sans-serif;font-size:10px;font-weight:600;letter-spacing:.5px;text-transform:uppercase;line-height:1.4}
.xtra-item .label{display:block}
.ico{width:38px;height:38px;border-radius:50%;border:1px solid var(--line);display:flex;align-items:center;justify-content:center;flex:none;background:#fff}

/* details */
.details{top:720px;height:720px;border-top:1px solid var(--line)}
.details .head{left:193px;top:100px}
.details .copy{left:193px;top:208px;width:500px}
.feat-grid{left:193px;top:400px;width:520px;display:grid;grid-template-columns:repeat(3,1fr);row-gap:42px}
.feat{display:flex;flex-direction:column;align-items:center;gap:12px;font-family:"Montserrat",Arial,sans-serif;font-size:10px;font-weight:600;letter-spacing:.5px;text-align:center;text-transform:uppercase;line-height:1.4}
.feat .ico{width:44px;height:44px}
.feat .ico.hl{background:var(--blue);border-color:var(--blue)}
.hand-product{left:700px;top:120px;width:500px;height:520px;background:
  radial-gradient(ellipse 18% 20% at 40% 32%,rgba(216,58,58,.55),rgba(216,58,58,0) 100%),
  radial-gradient(ellipse 30% 38% at 40% 35%,var(--device),rgba(244,246,248,0) 100%),
  radial-gradient(ellipse 45% 60% at 70% 50%,var(--skin),rgba(241,205,176,0) 100%)}

/* protect */
.protect{top:1440px;height:500px;background:radial-gradient(ellipse at 70% 40%,#34402f 0%,var(--dark) 70%)}
.protect-copy{left:327px;top:130px;width:330px;color:#fff}
.protect-copy .h-thin,.protect-copy .h-bold{font-size:21px}
.protect-copy p{font-size:12px;line-height:1.6;margin-top:14px;font-weight:600;color:#e8ebe6}
.protect-copy .btn{margin-top:26px}
.protect-product{left:745px;top:135px;width:180px;height:230px}
.fbox{position:absolute;background:#3a423a;color:#d9ddd7;font-family:"Montserrat",Arial,sans-serif;font-size:9px;font-weight:600;letter-spacing:.5px;padding:7px 10px;border:1px solid #5a625a;text-transform:uppercase}

/* reviews */
.reviews{top:1950px;height:650px}
.reviews .head{left:193px;top:76px}
.add-review{left:883px;top:130px;padding:8px 20px}
.review-row{left:193px;top:225px;width:814px;display:flex}
.review{flex:1;padding:0 30px;text-align:center;border-left:1px solid var(--line)}
.review:first-child{border-left:none}
.review h4{font-family:"Montserrat",Arial,sans-serif;font-size:11px;letter-spacing:1px;font-weight:700;text-transform:uppercase}
.review p{font-size:11.5px;line-height:1.65;color:var(--muted);margin-top:14px}
.stars{margin-top:16px;color:var(--blue);letter-spacing:3px;font-size:13px}
.avatar{width:40px;height:40px;border-radius:50%;background:linear-gradient(135deg,#d8c4b4,#9fa7b2);margin:22px auto 8px}
.review .who{font-family:"Montserrat",Arial,sans-serif;font-size:10px;font-weight:700;letter-spacing:.5px;text-transform:uppercase}
.review .when{font-size:9.5px;color:var(--muted);margin-top:3px}
.dots{left:585px;top:562px;display:flex;gap:6px}
.dots i{width:7px;height:7px;border-radius:50%;background:#d3d6db;display:block}
.dots i.on{background:var(--orange)}

/* videos */
.videos{top:2600px;height:613px;background:linear-gradient(180deg,#1f2420,#2a1c1a 60%,#1e2220)}
.videos .head{left:0;width:1200px;top:82px;text-align:center;color:#fff}
.video-frame{left:267px;top:183px;width:666px;height:344px;background:linear-gradient(180deg,#f3c87a 0%,#e59a4a 45%,#7b6b3c 75%,#4d5a2d 100%)}
.play{left:578px;top:333px;width:44px;height:44px;background:var(--blue);display:flex;align-items:center;justify-content:center}
.arrow{width:36px;height:36px;border-radius:50%;border:1.5px solid #fff;display:flex;align-items:center;justify-content:center;top:337px}
.thumbs{left:330px;top:542px;display:flex;gap:6px}
.thumb{width:72px;height:60px;background:#eef0f3;border:2px solid #fff}
.thumb.warm{background:linear-gradient(180deg,#f0c07a,#6f6a3a)}
.thumb.cool{background:radial-gradient(circle at 50% 45%,rgba(216,58,58,.45),rgba(216,58,58,0) 30%),linear-gradient(180deg,#ffffff,#c9d0d8)}

/* about */
.about{top:3213px;height:633px}
.about .head{left:193px;top:76px}
.about .copy{left:193px;top:188px;width:400px}
.about .aside{left:620px;top:234px;width:340px}
.about .aside h5{font-family:"Montserrat",Arial,sans-serif;font-size:11.5px;font-weight:700;letter-spacing:.6px;line-height:1.5;text-transform:uppercase}
.about-product{left:300px;top:320px;width:600px;height:260px;background:
  radial-gradient(ellipse 50% 40% at 50% 45%,var(--device) 0%,#e3e7eb 70%,rgba(201,208,216,0) 100%)}

/* contact */
.contact{top:3846px;height:622px;background:var(--blue);color:#fff}
.contact .head{left:193px;top:104px}
.contact .tag{border-color:#fff;color:#fff}
.contact-lead{left:193px;top:247px;width:420px;font-family:"Montserrat",Arial,sans-serif;font-weight:700;font-size:14px;line-height:1.55;letter-spacing:.5px;text-transform:uppercase}
.contact-list{left:193px;top:360px;list-style:none;font-size:11px;line-height:2.35}
.contact-list li{display:flex;align-items:center;gap:10px}
.socials{left:193px;top:485px;display:flex;gap:8px}
.socials i{width:26px;height:26px;border-radius:50%;border:1px solid rgba(255,255,255,.7);display:block}
.form{left:614px;top:222px;width:353px;display:flex;flex-direction:column;gap:10px}
.field{height:34px;border-radius:17px;background:#fff;color:#9aa3ae;font-size:10.5px;padding:0 16px;display:flex;align-items:center}
.field.area{height:82px;border-radius:14px;align-items:flex-start;padding-top:10px}
.submit{margin-top:12px;height:36px;border-radius:18px;border:1.5px solid #fff;display:flex;align-items:center;justify-content:center;font-family:"Montserrat",Arial,sans-serif;font-size:10.5px;font-weight:700;letter-spacing:1px}

/* newsletter */
.newsletter{top:4468px;height:88px;background:var(--mist);border-top:1px solid var(--line)}
.nl-label{left:193px;top:38px;font-family:"Montserrat",Arial,sans-serif;font-size:9px;font-weight:600;letter-spacing:.6px;color:var(--muted);text-transform:uppercase;white-space:nowrap}
.nl-input{left:450px;top:28px;width:200px;height:30px;background:#fff;border:1px solid var(--line);border-radius:15px}
.cards{left:805px;top:34px;display:flex;gap:5px}
.cards i{width:38px;height:20px;border-radius:3px;background:#cfd6df;display:block}

/* footer */
.footer{top:4556px;height:107px;background:#fff}
.footer .brand{position:absolute;left:193px;top:32px}
.footer small{position:absolute;left:193px;top:66px;font-size:9.5px;color:var(--muted)}
.to-top{left:988px;top:40px;width:26px;height:26px;border:1px solid var(--line);display:flex;align-items:center;justify-content:center}
</style>
</head>
<body>

<header class="hero">
  <svg class="hero-bg" width="1200" height="640" viewBox="0 0 1200 640" aria-hidden="true">
    <defs>
      <linearGradient id="heroFill" x1="0" y1="0" x2="1" y2="1">
        <stop offset="0" stop-color="#5b9cec"/>
        <stop offset="1" stop-color="#3f86e0"/>
      </linearGradient>
    </defs>
    <polygon points="0,0 1200,0 1200,515 600,605 0,515" fill="url(#heroFill)"/>
  </svg>
  <div class="abs" role="img" aria-label="Faint photo of an older man raising his arms in joy behind the headline" style="left:600px;top:90px;width:440px;height:440px;background:radial-gradient(ellipse at 60% 40%,rgba(255,255,255,.18),rgba(255,255,255,0) 70%)"></div>

  <div class="topbar">
    <span>CALL US: 1-800-555-0142 &nbsp;·&nbsp; HELLO@ELDERHARBORCIRCLE.COM</span>
    <span>SIGN IN &nbsp;&nbsp;&nbsp; REGISTER</span>
  </div>

  <nav class="nav">
    <div class="brand"><span class="brand-dot"></span>Elder Harbor Circle</div>
    <div class="menu">
      <span class="on">HOME</span><span>FEATURES</span><span>GALLERY</span><span>SPECS</span><span>REVIEWS</span><span>NEWS</span><span>ABOUT</span><span>CONTACT</span>
    </div>
    <span class="btn btn-orange" style="padding:9px 18px;font-size:10px">BUY NOW</span>
  </nav>

  <div class="abs device-photo hero-product" role="img" aria-label="Product photo of the white personal alert device with red cross help button and its reflection"></div>

  <div class="abs hero-copy">
    <div class="kicker">MADE FOR YOUR HELP</div>
    <h1 class="hero-title">AMERICA'S #1 RATED<br>PROTECTION NETWORK</h1>
    <p>Lorem ipsum dolor sit amet, consectetur adipisicing elit, sed do eiusmod tempor incididunt ut labore et dolore.</p>
    <div class="hero-btns">
      <span class="btn btn-ghost">&#9654;&nbsp; WATCH THE VIDEO</span>
      <span class="btn btn-ghost">LEARN MORE</span>
    </div>
  </div>
</header>

<section class="xtra">
  <div class="xtra-inner">
    <div class="xtra-title">XTRA<b>FEATURES</b></div>
    <div class="xtra-item"><span class="ico"><svg width="16" height="16" viewBox="0 0 16 16"><path d="M8 1a5 5 0 0 0-5 5c0 4 5 9 5 9s5-5 5-9a5 5 0 0 0-5-5z" fill="none" stroke="#7a808a" stroke-width="1.2"/><circle cx="8" cy="6" r="1.8" fill="#7a808a"/></svg></span><span class="label">Quick GPS<br>Help</span></div>
    <div class="xtra-item"><span class="ico"><svg width="16" height="16" viewBox="0 0 16 16"><circle cx="8" cy="9" r="5.5" fill="none" stroke="#7a808a" stroke-width="1.2"/><path d="M8 6v3l2 1.5" stroke="#7a808a" stroke-width="1.2" fill="none"/></svg></span><span class="label">Timer<br>&amp; Alarm</span></div>
    <div class="xtra-item"><span class="ico"><svg width="16" height="16" viewBox="0 0 16 16"><path d="M8 1.5 2.5 4v4c0 3.5 2.5 5.8 5.5 6.5 3-.7 5.5-3 5.5-6.5V4z" fill="none" stroke="#7a808a" stroke-width="1.2"/></svg></span><span class="label">Invisible<br>Protection Alert</span></div>
    <div class="xtra-item"><span class="ico"><svg width="16" height="16" viewBox="0 0 16 16"><path d="M3 13 8 3l5 10z" fill="none" stroke="#7a808a" stroke-width="1.2"/><path d="M8 7v3" stroke="#7a808a" stroke-width="1.2"/></svg></span><span class="label">Automatic<br>Fall Detection</span></div>
  </div>
</section>

<section class="details">
  <div class="abs hand-product" role="img" aria-label="Photo of a hand holding the white alert device with red cross button"></div>
  <div class="abs head">
    <div class="h-thin">Senior Protection</div>
    <div class="h-bold">In Details</div>
    <div class="tag" style="margin-top:14px">Key Features</div>
  </div>
  <div class="abs copy body-text">
    <p>Lorem ipsum dolor sit amet consectetur adipiscing elit sed do eiusmod tempor incididunt ut labore et dolore magna aliqua. Ut enim ad minim veniam quis nostrud exercitation ullamco laboris nisi ut aliquip ex ea commodo consequat. Duis aute irure dolor reprehenderit in voluptate velit esse cillum fugiat nulla pariatur.</p>
    <p style="margin-top:14px">Excepteur sint occaecat cupidatat non proident sunt in culpa qui officia.</p>
  </div>
  <div class="abs feat-grid">
    <div class="feat"><span class="ico"><svg width="18" height="18" viewBox="0 0 18 18"><path d="M4 7a5 5 0 0 1 9-2M14 11a5 5 0 0 1-9 2" fill="none" stroke="#7a808a" stroke-width="1.3"/><path d="M13 2v3h-3M5 16v-3h3" fill="none" stroke="#7a808a" stroke-width="1.3"/></svg></span><span>Auto Sync</span></div>
    <div class="feat"><span class="ico"><svg width="18" height="18" viewBox="0 0 18 18"><path d="M3 7h3l4-3v10l-4-3H3z" fill="none" stroke="#7a808a" stroke-width="1.3"/><path d="M12.5 6.5a3.5 3.5 0 0 1 0 5" fill="none" stroke="#7a808a" stroke-width="1.3"/></svg></span><span>Audio Prompts</span></div>
    <div class="feat"><span class="ico"><svg width="18" height="18" viewBox="0 0 18 18"><circle cx="5" cy="9" r="2" fill="none" stroke="#7a808a" stroke-width="1.3"/><circle cx="13" cy="4.5" r="2" fill="none" stroke="#7a808a" stroke-width="1.3"/><circle cx="13" cy="13.5" r="2" fill="none" stroke="#7a808a" stroke-width="1.3"/><path d="m7 8 4-2.5M7 10l4 2.5" stroke="#7a808a" stroke-width="1.3"/></svg></span><span>Activity Tracker</span></div>
    <div class="feat"><span class="ico"><svg width="18" height="18" viewBox="0 0 18 18"><rect x="3" y="4" width="12" height="9" rx="1.5" fill="none" stroke="#7a808a" stroke-width="1.3"/><path d="m3 5 6 4 6-4" fill="none" stroke="#7a808a" stroke-width="1.3"/></svg></span><span>Advanced<br>Notifications</span></div>
    <div class="feat"><span class="ico hl"><svg width="20" height="14" viewBox="0 0 20 14"><rect x="1" y="2" width="16" height="10" rx="2" fill="none" stroke="#fff" stroke-width="1.4"/><rect x="17.5" y="5" width="2" height="4" fill="#fff"/><rect x="3" y="4" width="9" height="6" fill="#fff"/></svg></span><span>30 Days<br>Battery Time</span></div>
    <div class="feat"><span class="ico"><svg width="18" height="18" viewBox="0 0 18 18"><circle cx="9" cy="9" r="3" fill="none" stroke="#7a808a" stroke-width="1.3"/><path d="M9 1.5v2.5M9 14v2.5M1.5 9H4M14 9h2.5M3.7 3.7l1.8 1.8M12.5 12.5l1.8 1.8M3.7 14.3l1.8-1.8M12.5 5.5l1.8-1.8" stroke="#7a808a" stroke-width="1.3"/></svg></span><span>Readable in<br>Sunlight</span></div>
  </div>
</section>

<section class="protect">
  <div class="abs" role="img" aria-label="Dark green background photo of grass with a faint open hand" style="inset:0;background:linear-gradient(180deg,rgba(40,52,36,.3),rgba(20,26,20,.55))"></div>
  <div class="abs protect-copy">
    <div class="h-thin">Protect Family</div>
    <div class="h-bold">&amp; Independence</div>
    <p>Lorem ipsum dolor sit amet consectetur adipiscing elit sed do eiusmod tempor incididunt ut labore et dolore magna aliqua enim ad minim veniam quis nostrud exercitation ullamco laboris nisi ut aliquip.</p>
    <span class="btn btn-orange">BUY IT NOW - $99</span>
  </div>
  <svg class="abs" style="left:620px;top:60px" width="440" height="380" viewBox="0 0 440 380" aria-hidden="true">
    <g stroke="#7d857b" stroke-width="1" fill="none">
      <path d="M95 70 H140"/><path d="M245 40 V75"/><path d="M270 100 H320 V150"/><path d="M330 245 H290"/><path d="M175 265 V300"/>
    </g>
    <g fill="#e88">
      <circle cx="140" cy="70" r="3.5"/><circle cx="245" cy="75" r="3.5"/><circle cx="270" cy="100" r="3.5"/><circle cx="290" cy="245" r="3.5"/><circle cx="175" cy="265" r="3.5"/>
    </g>
  </svg>
  <div class="abs device-photo protect-product" role="img" aria-label="Photo of the alert device standing upright"></div>
  <span class="fbox" style="left:648px;top:115px">Feature</span>
  <span class="fbox" style="left:838px;top:68px">Feature</span>
  <span class="fbox" style="left:910px;top:195px">Feature</span>
  <span class="fbox" style="left:955px;top:302px">Feature</span>
  <span class="fbox" style="left:742px;top:358px">Feature</span>
</section>

<section class="reviews">
  <div class="abs head">
    <div class="h-thin">Senior Protection</div>
    <div class="h-bold">User Reviews</div>
    <div class="tag" style="margin-top:14px">Testimonials</div>
  </div>
  <span class="abs btn btn-line add-review">Add your review</span>
  <div class="abs review-row">
    <article class="review">
      <h4>Great Device</h4>
      <p>Lorem ipsum dolor sit amet adipiscing elit sed tempor incididunt ut labore et dolore magna aliqua enim veniam quis nostrud ullamco laboris.</p>
      <div class="stars">★★★★★</div>
      <div class="avatar" role="img" aria-label="Reviewer portrait"></div>
      <div class="who">Nora Whitfield</div><div class="when">Portland · 12 October 2017</div>
    </article>
    <article class="review">
      <h4>Fantastic Protection</h4>
      <p>Lorem ipsum dolor sit amet adipiscing elit sed tempor incididunt ut labore et dolore magna aliqua enim veniam quis nostrud ullamco laboris.</p>
      <div class="stars">★★★★☆</div>
      <div class="avatar" role="img" aria-label="Reviewer portrait"></div>
      <div class="who">Elise Moran</div><div class="when">Salem · 18 October 2017</div>
    </article>
    <article class="review">
      <h4>Keep Me Safe</h4>
      <p>Lorem ipsum dolor sit amet adipiscing elit sed tempor incididunt ut labore et dolore magna aliqua enim veniam quis nostrud ullamco laboris.</p>
      <div class="stars">★★★★★</div>
      <div class="avatar" role="img" aria-label="Reviewer portrait"></div>
      <div class="who">Theo Hale</div><div class="when">Dover · 24 October 2017</div>
    </article>
  </div>
  <div class="abs dots"><i class="on"></i><i></i><i></i></div>
</section>

<section class="videos">
  <div class="abs" role="img" aria-label="Dark background photo of a family flying a red kite" style="inset:0;background:radial-gradient(ellipse at 30% 40%,rgba(160,40,40,.25),rgba(0,0,0,0) 60%)"></div>
  <div class="abs head">
    <div class="h-thin">Senior Protection</div>
    <div class="h-bold">Videos &amp; Images</div>
  </div>
  <div class="abs video-frame" role="img" aria-label="Video still of a family walking in a field at sunset"></div>
  <div class="abs play"><svg width="14" height="16" viewBox="0 0 14 16"><path d="M1 1l12 7-12 7z" fill="#fff"/></svg></div>
  <div class="abs arrow" style="left:210px"><svg width="10" height="12" viewBox="0 0 10 12"><path d="M8 1 2 6l6 5" fill="none" stroke="#fff" stroke-width="1.6"/></svg></div>
  <div class="abs arrow" style="left:954px"><svg width="10" height="12" viewBox="0 0 10 12"><path d="m2 1 6 5-6 5" fill="none" stroke="#fff" stroke-width="1.6"/></svg></div>
  <div class="abs thumbs" role="img" aria-label="Gallery thumbnails of family photos and the device">
    <div class="thumb cool"></div><div class="thumb warm"></div><div class="thumb warm"></div><div class="thumb cool"></div><div class="thumb cool"></div><div class="thumb warm"></div><div class="thumb cool"></div>
  </div>
</section>

<section class="about">
  <div class="abs head">
    <div class="h-thin">Senior Protection</div>
    <div class="h-bold">About Us</div>
    <div class="tag" style="margin-top:14px">The Company</div>
  </div>
  <div class="abs copy body-text">Lorem ipsum dolor sit amet consectetur adipiscing elit sed do eiusmod tempor incididunt ut labore et dolore magna aliqua. Ut enim ad minim veniam quis nostrud exercitation ullamco laboris nisi ut aliquip ex ea commodo consequat. Duis aute irure dolor in reprehenderit in voluptate velit esse cillum dolore eu fugiat nulla pariatur excepteur sint occaecat.</div>
  <div class="abs aside">
    <h5>We are a new &amp; trusted name in smartwatch advanced technology</h5>
    <p class="body-text" style="margin-top:8px;font-size:11px">Lorem ipsum dolor sit amet consectetur adipiscing elit sed do eiusmod tempor incididunt ut labore.</p>
  </div>
  <div class="abs about-product" role="img" aria-label="Photo of the white alert device lying flat, side view"></div>
</section>

<section class="contact">
  <div class="abs head">
    <div class="h-thin">Senior Protection</div>
    <div class="h-bold">Contact Us</div>
    <div class="tag" style="margin-top:14px">Get in touch</div>
  </div>
  <div class="abs contact-lead">Have a question? Give us a call or fill out the contact form – we'd love to hear from you</div>
  <ul class="abs contact-list">
    <li><svg width="12" height="12" viewBox="0 0 12 12"><path d="M6 1a3.5 3.5 0 0 0-3.5 3.5C2.5 7.5 6 11 6 11s3.5-3.5 3.5-6.5A3.5 3.5 0 0 0 6 1z" fill="#fff"/></svg>28 Harbor Lane, Portsmouth</li>
    <li><svg width="12" height="12" viewBox="0 0 12 12"><path d="M2 1h2.5l1 2.5L4 5a7 7 0 0 0 3 3l1.5-1.5 2.5 1V11C6 11 1 6 1 2z" fill="#fff"/></svg>Phone: +1 800 555 0142</li>
    <li><svg width="12" height="12" viewBox="0 0 12 12"><rect x="1.5" y="3" width="9" height="6.5" fill="#fff"/><rect x="3" y="1" width="6" height="2.5" fill="#fff"/></svg>Fax: +1 800 555 0143</li>
    <li><svg width="12" height="12" viewBox="0 0 12 12"><rect x="1" y="2.5" width="10" height="7" fill="#fff"/><path d="m1 3 5 3.5L11 3" stroke="#4a8fe7" fill="none"/></svg>Email: hello@elderharborcircle.com</li>
  </ul>
  <div class="abs socials"><i></i><i></i><i></i><i></i><i></i><i></i></div>
  <div class="abs form">
    <div class="field">Your Name</div>
    <div class="field">Email Address</div>
    <div class="field">Subject</div>
    <div class="field area">Your Comment</div>
    <div class="submit">SUBMIT COMMENT</div>
  </div>
</section>

<section class="newsletter">
  <div class="abs nl-label">Get the Elder Harbor Circle updates by email</div>
  <div class="abs nl-input"></div>
  <div class="abs cards"><i></i><i></i><i></i><i></i><i></i></div>
</section>

<footer class="footer">
  <div class="brand"><span class="brand-dot"></span>Elder Harbor Circle</div>
  <small>© Copyright 2017. All rights reserved.</small>
  <div class="abs to-top"><svg width="10" height="8" viewBox="0 0 10 8"><path d="M1 7 5 2l4 5" fill="none" stroke="#7a808a" stroke-width="1.4"/></svg></div>
</footer>

</body>
</html>
```